velto renovation roof

We need a flyer for a new york based company called velto renovations. We are looking to promote our roofing/window/siding/concrete service.

We are a construction company with over 30 years in the business, but have set up a new company to specialize in roofing - windows - siding. We do offer general renovation service both interior (tiles, paint , Plakwall, etc) as well as concrete work (driveways, sidewalk) but we think it may be to much information for the flyer. We are fully insured and licensed

We are open to all ideas (I will include a picture of a design that caught our eye from your site).

Target Market(s)

home owners, building managers in the tri state area. We are a New York based company

Industry/Entity Type

Construction

```html
<!DOCTYPE html>
<html lang="en">
<head>
<meta charset="utf-8">
<title>Velto Renovations – Flyers</title>
<link rel="stylesheet" href="https://fonts.googleapis.com/css2?family=Oswald:wght@500;600&family=Roboto+Condensed:wght@400;700&family=Arimo:wght@400;700&display=swap">
<style>
  :root{
    --backdrop:#1d1d1f;
    --brand-blue:#1d6fbf;
    --brand-blue-dark:#155a9f;
    --sky:#0aa8ec;
    --sky-soft:#36b6ef;
    --sun:#f9c21b;
    --red:#d42a2a;
    --ink:#2c2c2c;
    --white:#ffffff;
  }
  *{box-sizing:border-box;margin:0;padding:0}
  html,body{width:1200px;height:1000px;overflow:hidden;background:var(--backdrop)}
  .canvas{position:relative;width:1200px;height:1000px}

  .flyer{position:absolute;left:148px;width:904px;height:426px;background:var(--brand-blue);overflow:hidden;box-shadow:0 6px 18px rgba(0,0,0,.5)}
  .flyer--services{top:67px}
  .flyer--specialties{top:507px}

  .brand{position:absolute;left:36px;width:360px;text-align:center;color:var(--white);font-family:"Oswald",sans-serif;font-weight:600;line-height:1}
  .brand__top{display:block;font-size:44px;letter-spacing:2px}
  .brand__main{display:block;font-size:64px;letter-spacing:-1px;margin-top:4px}
  .flyer--services .brand{top:62px}
  .flyer--specialties .brand{top:58px}

  .tagline{position:absolute;left:32px;width:357px;height:30px;background:var(--sun);color:var(--ink);font-family:"Roboto Condensed",sans-serif;font-size:14.5px;display:flex;align-items:center;justify-content:center}
  .flyer--services .tagline{top:197px}
  .flyer--specialties .tagline{top:200px}

  .offer{position:absolute;left:27px;top:243px;width:370px;height:125px}
  .offer svg{position:absolute;inset:0}
  .offer__text{position:absolute;left:0;right:0;top:30px;text-align:center;font-family:"Roboto Condensed",sans-serif;color:var(--white);font-weight:700;font-size:13px;line-height:1.2}
  .offer__title{display:block;font-family:"Oswald",sans-serif;font-weight:500;font-size:24px;color:var(--sun);line-height:1.05;margin-bottom:1px}

  .swoosh{position:absolute;inset:0}

  .gallery{position:absolute;left:427px;top:33px;display:grid;grid-template-columns:220px 220px;grid-template-rows:153px 155px;gap:7px 5px}
  .gallery__photo{border:6px solid var(--white);box-shadow:0 2px 6px rgba(0,0,0,.35)}
  .photo--family{background:linear-gradient(180deg,#cfe3f3 0%,#e9eef0 45%,#7fae5a 100%)}
  .photo--roof{background:linear-gradient(160deg,#e6d2bd 0%,#8a6f5a 40%,#4c4a4a 100%)}
  .photo--tiles{background:linear-gradient(90deg,#e8b9a6 0%,#f3f1ee 45%,#d9d4cf 100%)}
  .photo--painter{background:linear-gradient(180deg,#f4f5f6 0%,#dfe4e8 60%,#3b5678 100%)}

  .contact{position:absolute;left:0;bottom:0;width:100%;height:63px;background:var(--white);display:flex;align-items:center;padding-left:30px;font-family:"Arimo",sans-serif;font-size:16px;color:var(--ink)}
  .contact__item{display:flex;align-items:center;gap:12px}
  .contact__item strong{font-weight:700}
  .contact__divider{width:1.5px;height:28px;background:#333;margin:0 16px}
  .icon{width:20px;height:26px;flex:none}
  .icon--globe{width:30px;height:30px}
  .flyer--services .contact{padding-top:0}
  .flyer--services .contact__wrap{position:relative;display:flex;align-items:center}

  .tool-house{position:absolute;left:412px;top:40px;width:450px;height:440px;border-radius:50%;background:var(--sky);padding:6px}
  .tool-house__art{width:100%;height:100%;border-radius:50%;background:radial-gradient(circle at 50% 45%,#ffffff 0%,#ffffff 55%,#f2f2f2 100%);position:relative}
  .tool-house__art span{position:absolute;left:115px;top:15px;width:200px;height:200px;background:linear-gradient(160deg,#e7d3b3 0%,#b98b54 35%,#9fa7ad 70%,#3d6db0 100%);opacity:.55;border-radius:4px}

  .specialty-band{position:absolute;left:0;top:253px;width:100%;height:93px;background:var(--sky);display:flex;align-items:center;color:var(--white);font-family:"Arimo",sans-serif;font-weight:700}
  .specialty-band__lead{font-size:19px;margin-left:39px}
  .specialty-band__arrow{margin:0 12px 0 10px}
  .specialty-band__list{font-size:33px;line-height:1.2;letter-spacing:-.3px;text-shadow:0 1px 2px rgba(0,0,0,.25)}
  .flyer--specialties .contact{height:65px;padding-left:40px}
</style>
</head>
<body>
<main class="canvas">

  <section class="flyer flyer--services">
    <svg class="swoosh" width="904" height="426" viewBox="0 0 904 426" aria-hidden="true">
      <path d="M904 228 C800 250 720 300 640 363 L904 363 Z" fill="var(--sky)"/>
      <path d="M904 245 C820 262 740 310 668 363 L904 363 Z" fill="var(--sky-soft)" opacity=".6"/>
    </svg>

    <h1 class="brand"><span class="brand__top">VELTO</span><span class="brand__main">RENOVATIONS</span></h1>
    <p class="tagline">Construction company with over 30 years in the business</p>

    <div class="offer">
      <svg width="370" height="125" viewBox="0 0 370 125" aria-hidden="true">
        <polygon fill="var(--red)" points="370,125 359.5,110.9 363.7,94.5 347.6,83.7 345.2,66 324.6,59.2 315.8,41.6 292.1,39.3 277.5,22.8 252.4,25.2 232.9,11 208,17.9 185,7 162,17.9 137.1,11 117.6,25.2 92.5,22.8 77.9,39.3 54.2,41.6 45.4,59.2 24.8,66 22.4,83.7 6.3,94.5 10.5,110.9 0,125"/>
      </svg>
      <p class="offer__text"><span class="offer__title">WE DO OFFER</span>general renovation service both interior<br>(tiles, paint , Plakwall, etc) as well as<br>concrete work (driveways, sidewalk)</p>
    </div>

    <div class="gallery">
      <div class="gallery__photo photo--family" role="img" aria-label="Photo of a smiling family standing in front of their suburban house"></div>
      <div class="gallery__photo photo--roof" role="img" aria-label="Photo of two roofers installing shingles on a pitched roof"></div>
      <div class="gallery__photo photo--tiles" role="img" aria-label="Photo of a woman setting wall tiles"></div>
      <div class="gallery__photo photo--painter" role="img" aria-label="Photo of a painter on a ladder in a bright room with windows"></div>
    </div>

    <footer class="contact">
      <svg width="904" height="63" viewBox="0 0 904 63" style="position:absolute;left:0;top:0" aria-hidden="true">
        <path d="M904 0 L904 63 L470 63 C560 55 620 20 660 0 Z" fill="var(--sky)"/>
        <path d="M904 0 L904 63 L500 63 C590 52 640 20 690 0 Z" fill="var(--brand-blue)" opacity=".9"/>
      </svg>
      <div class="contact__wrap">
        <span class="contact__item">
          <svg class="icon" viewBox="0 0 20 26" aria-hidden="true"><rect x="3" y="1" width="14" height="24" rx="3" fill="none" stroke="var(--brand-blue)" stroke-width="2.4"/><rect x="7" y="20" width="6" height="2" fill="var(--brand-blue)"/></svg>
          <span>Phone: <strong>555-014-2870</strong></span>
        </span>
        <span class="contact__divider"></span>
        <span class="contact__item">
          <svg class="icon icon--globe" viewBox="0 0 30 30" aria-hidden="true"><g fill="none" stroke="var(--brand-blue)" stroke-width="2"><circle cx="15" cy="15" r="13"/><ellipse cx="15" cy="15" rx="6" ry="13"/><path d="M2 15h26M4 8h22M4 22h22M15 2v26"/></g></svg>
          <strong>www.VELTORENO.net</strong>
        </span>
      </div>
    </footer>
  </section>

  <section class="flyer flyer--specialties">
    <div class="tool-house">
      <div class="tool-house__art" role="img" aria-label="Illustration of hand tools – hammer, saw, screwdrivers, square and brush – arranged into the outline of a house"><span></span></div>
    </div>

    <h2 class="brand"><span class="brand__top">VELTO</span><span class="brand__main">RENOVATIONS</span></h2>
    <p class="tagline">Construction company with over 30 years in the business</p>

    <div class="specialty-band">
      <span class="specialty-band__lead">WE ARE SPECIALIZE IN</span>
      <svg class="specialty-band__arrow" width="50" height="30" viewBox="0 0 50 30" aria-hidden="true"><path d="M0 9h30V1l19 14-19 14v-8H0z" fill="var(--sun)"/></svg>
      <p class="specialty-band__list">ROOFING • WINDOWS<br>SIDING • CONCRETE SERVICE</p>
    </div>

    <footer class="contact">
      <span class="contact__item">
        <svg class="icon" viewBox="0 0 20 26" aria-hidden="true"><rect x="3" y="1" width="14" height="24" rx="3" fill="none" stroke="var(--brand-blue)" stroke-width="2.4"/><rect x="7" y="20" width="6" height="2" fill="var(--brand-blue)"/></svg>
        <span>Phone: <strong>555-014-2870</strong></span>
      </span>
      <span class="contact__divider" style="margin:0 24px"></span>
      <span class="contact__item">
        <svg class="icon icon--globe" viewBox="0 0 30 30" aria-hidden="true"><g fill="none" stroke="var(--brand-blue)" stroke-width="2"><circle cx="15" cy="15" r="13"/><ellipse cx="15" cy="15" rx="6" ry="13"/><path d="M2 15h26M4 8h22M4 22h22M15 2v26"/></g></svg>
        <strong>www.VELTORENO.net</strong>
      </span>
      <span class="contact__divider" style="margin:0 24px"></span>
      <strong class="contact__item">We are fully insured and licensed</strong>
    </footer>
  </section>

</main>
</body>
</html>
```